New Website for ReBranded Company - CrewBeacon

We have a successful company and website currently but it is a little dated. We have re-branded the company from Harbor Signal Networks to CrewBeacon and have a new logo for the new name. We are looking to build a newer fresher website with the new name. I will need a concept of the home page and one inside page. You can see our current site at https://www.harborsignalnetworks.example and the new site will be https://www.crewbeacon.example .

I also really like the https://www.pathlantern.example/ website. I like ledgerkite.example website. I like the https://skillorbit.example/ website.

See the attached document for layout and some text to use. Use the pictures I attached as opposed to pictures from the old site as much as you can.

Target Market(s)

Business

Industry/Entity Type

Software Service

Number of Pages Required

2 page

Font styles to use
Sans Serif

Requirements
Must have
• Use the colors from my logo. Professional but modern. We want people to feel like our product makes their staff feel safer at work.
Should not have
• Don't use any red or orange (no stop colors).

```html
<!DOCTYPE html>
<html lang="en">
<head>
<meta charset="utf-8">
<title>CrewBeacon – Feel Confident That Your Staff Is Protected</title>
<link rel="stylesheet" href="https://fonts.googleapis.com/css2?family=Lexend:wght@300;400;500;600;700&display=swap">
<style>
:root{
  --blue:#0f67b1;
  --blue-deep:#0b4f92;
  --green:#52b404;
  --green-soft:#4aa80f;
  --navy:#0c2b47;
  --navy-dark:#071e35;
  --white:#ffffff;
  --ink:#0f67b1;
}
*{margin:0;padding:0;box-sizing:border-box}
html,body{width:1200px;height:3759px;overflow:hidden}
body{font-family:"Lexend",sans-serif;background:var(--white);position:relative;color:var(--ink)}
.abs{position:absolute}
.center{left:0;width:1200px;text-align:center}
.btn{position:absolute;display:flex;align-items:center;justify-content:center;border-radius:24px;font-weight:600;font-size:20px;text-decoration:none}
.btn-white{background:var(--white);color:var(--blue)}
.btn-green{background:var(--green);color:var(--white)}
.btn-blue{background:var(--blue);color:var(--white);border-radius:36px;font-size:25px;letter-spacing:.5px;box-shadow:0 6px 14px rgba(15,103,177,.3)}
.dot-icon{position:absolute;width:52px;height:52px;border-radius:50%;background:var(--white)}
.divider-dot{position:absolute;left:571px;width:58px;height:58px;border-radius:50%;background:var(--white);box-shadow:0 6px 12px rgba(0,0,0,.15)}

/* header */
.site-header{position:absolute;top:0;left:0;width:1200px;height:69px;background:var(--white)}
.brand{position:absolute;left:136px;top:14px;display:flex;align-items:center;gap:10px;font-size:26px;font-weight:500;color:var(--blue)}
.brand i{width:36px;height:36px;border-radius:50%;background:var(--blue);display:block}
.nav a{position:absolute;top:25px;font-size:16px;font-weight:500;text-decoration:none}
.nav .home{left:434px;color:var(--blue)}
.nav .addons{left:521px;color:var(--green)}
.nav .login{left:658px;color:var(--blue)}
.nav .explore{left:860px;top:13px;width:203px;height:42px;border:1.5px solid var(--blue);border-radius:4px;display:flex;align-items:center;justify-content:center;font-size:16px;color:var(--blue)}

/* hero */
.hero{position:absolute;top:69px;left:0;width:1200px;height:635px;background:linear-gradient(180deg,#1d6bb8 0%,#0f5ea8 55%,#0c5aa2 100%)}
.hero-title{top:206px;font-size:41px;font-weight:500;color:var(--white)}
.hero-sub{top:278px;font-size:27px;font-weight:300;color:var(--white)}
.hero-feature{position:absolute;top:530px;font-size:18px;line-height:24px;color:var(--white);font-weight:300;width:300px}
.hero-feature small{font-size:15px}

/* problem */
.problem-title{top:806px;font-size:40px;line-height:52px;font-weight:600;color:var(--blue)}
.problem-q{top:940px;font-size:26px;font-weight:500;color:var(--blue)}
.problem-s{top:1008px;font-size:27px;font-weight:300;color:var(--blue)}

/* why */
.why{position:absolute;top:1218px;left:0;width:1200px;height:617px;background:var(--green)}
.why-title{top:1298px;font-size:47px;font-weight:600;color:var(--white)}
.why-col{position:absolute;top:1480px;width:260px;color:var(--white)}
.why-col h3{font-size:32px;line-height:36px;font-weight:500;margin-bottom:18px}
.why-col p{font-size:15px;line-height:24px;font-weight:600}
.why-col .opts{display:grid;grid-template-columns:128px 110px;font-size:12px;line-height:15px;font-weight:600;margin-top:6px}

/* stats */
.stats{position:absolute;top:1835px;left:0;width:1200px;height:446px;background:linear-gradient(100deg,#0d5ea9 0%,#18839a 45%,#3ea33c 75%,#50b20a 100%)}
.stats-lead{left:137px;top:1948px;font-size:37px;line-height:41px;font-weight:500;color:var(--white);width:440px}
.stats-right{left:634px;top:1944px;font-size:28px;line-height:36px;font-weight:500;color:var(--white);width:440px}
.num{position:absolute;font-size:104px;font-weight:600;color:var(--white);line-height:1}
.num-label{position:absolute;font-size:28px;font-weight:500;color:var(--white)}

/* plan */
.plan-title{top:2336px;font-size:50px;font-weight:600;color:var(--blue)}
.step-card{position:absolute;background:var(--white);box-shadow:4px 4px 14px rgba(0,0,0,.08);color:var(--blue)}
.step-card h3{font-size:38px;font-weight:500;line-height:51px}
.step-card li{list-style:none;font-size:27px;line-height:34px;font-weight:300}
.step-num{position:absolute;width:68px;height:68px;border-radius:50%;background:var(--green);color:var(--white);font-size:44px;font-weight:600;display:flex;align-items:center;justify-content:center}

/* cta band */
.cta-band{position:absolute;top:3336px;left:0;width:1200px;height:102px;background:linear-gradient(90deg,#0f67b1 0%,#1c86a0 50%,#52b404 100%)}
.cta-band p{position:absolute;left:139px;top:34px;font-size:27px;font-weight:500;color:var(--white)}

/* footer */
.site-footer{position:absolute;top:3438px;left:0;width:1200px;height:270px;background:var(--navy)}
.foot-col{position:absolute;text-align:center;color:var(--white)}
.foot-col h4{font-size:24px;font-weight:500;color:var(--green);margin-bottom:10px}
.foot-col li{list-style:none;font-size:12px;line-height:24px;font-weight:500}
.foot-rule{position:absolute;top:3487px;width:1px;height:134px;background:rgba(255,255,255,.5)}
.legal{position:absolute;top:3708px;left:0;width:1200px;height:51px;background:var(--navy-dark);color:var(--white);font-size:15px}
</style>
</head>
<body>

<header class="site-header">
  <div class="brand"><i></i>CrewBeacon</div>
  <nav class="nav">
    <a class="home" href="#">Home</a>
    <a class="addons" href="#">Buy Add Ons</a>
    <a class="login" href="#">Customer Login</a>
    <a class="explore" href="#">Explore Your Choices</a>
  </nav>
</header>

<section class="hero" role="img" aria-label="Staff member wearing an electronic panic button on a lanyard, tinted blue"></section>
<h1 class="abs center hero-title">Feel Confident that your staff is protected</h1>
<p class="abs center hero-sub">Get a revolutionary new electronic panic button</p>
<a class="btn btn-white" href="#" style="left:460px;top:347px;width:283px;height:47px">Ready To Get Started</a>

<span class="dot-icon" style="left:137px;top:462px"></span>
<span class="dot-icon" style="left:483px;top:462px"></span>
<span class="dot-icon" style="left:810px;top:462px"></span>
<p class="hero-feature" style="left:137px">Problems Stopped Before They Start For Any Type Of Organization</p>
<p class="hero-feature" style="left:483px">Affordable Prices Starting at $18 per month.<br><small>No Contracts. No Hidden Costs.</small></p>
<p class="hero-feature" style="left:810px">Alerts by computer, mobile device, text, phone, email, monitoring and E911</p>
<span class="divider-dot" style="top:672px"></span>

<h2 class="abs center problem-title">Your Employess Shouldn’t Feel Alone When<br>They Need Help</h2>
<p class="abs center problem-q">Does this problem make you feel frustrated and anxious?</p>
<p class="abs center problem-s">Put a simple solution in their hands</p>
<a class="btn btn-green" href="#" style="left:463px;top:1072px;width:274px;height:46px">Ready To Get Started</a>

<section class="why"></section>
<span class="divider-dot" style="top:1189px"></span>
<h2 class="abs center why-title">Why Businesses Choose Us</h2>
<span class="dot-icon" style="left:138px;top:1408px"></span>
<span class="dot-icon" style="left:484px;top:1408px"></span>
<span class="dot-icon" style="left:809px;top:1408px"></span>
<div class="why-col" style="left:138px">
  <h3>Easy To Use</h3>
  <p>Press a button and let the right people know you need help and open a chat window letting everyone talk on resolving their problem.</p>
</div>
<div class="why-col" style="left:484px">
  <h3>Communicate What You Want</h3>
  <p style="font-size:13px">We give you lots of options:</p>
  <div class="opts"><span>Computer<br>Mobile<br>Email<br>Phone call</span><span>Text<br>E911<br>Call Center</span></div>
</div>
<div class="why-col" style="left:809px;width:250px">
  <h3>Cost Effective Protection</h3>
  <p style="font-size:13px">By leveraging your existing network and equipment we can lower your costs to give better options to your staff</p>
</div>
<a class="btn btn-white" href="#" style="left:458px;top:1702px;width:285px;height:47px">Ready To Get Started</a>

<section class="stats"></section>
<span class="divider-dot" style="top:1806px"></span>
<p class="abs stats-lead">We know how scary it can feel to worry about employee safety.</p>
<a class="btn btn-white" href="#" style="left:137px;top:2100px;width:286px;height:46px">Start My Demo</a>
<p class="abs stats-right">That’s why we have provided a way for customers to get help to staff effectively in</p>
<span class="num" style="left:636px;top:2068px">45</span>
<span class="num-label" style="left:788px;top:2098px;font-weight:300">Covering</span>
<span class="num" style="left:964px;top:2068px">5</span>
<span class="num-label" style="left:653px;top:2160px">States</span>
<span class="num-label" style="left:926px;top:2160px">Countries</span>
<span class="divider-dot" style="top:2252px"></span>

<h2 class="abs center plan-title">Simple Starter Plan</h2>
<svg class="abs" style="left:0;top:0" width="1200" height="3759" aria-hidden="true">
  <path d="M130 2460 C118 2580 170 2630 258 2648" fill="none" stroke="#cfd4d8" stroke-width="3" stroke-dasharray="8 7"/>
  <polygon points="266,2651 250,2641 252,2658" fill="#cfd4d8"/>
  <path d="M292 2688 C278 2850 400 2902 504 2908" fill="none" stroke="#cfd4d8" stroke-width="3" stroke-dasharray="8 7"/>
  <polygon points="514,2910 498,2900 498,2919" fill="#cfd4d8"/>
</svg>
<div class="step-card" style="left:131px;top:2424px;width:523px;height:179px;padding:30px 0 0 46px">
  <h3>Explore Your Choices</h3>
  <ul style="display:grid;grid-template-columns:235px 200px"><li>• Pricing</li><li>• Quote</li><li>• Trial</li><li>• Hardware</li></ul>
</div>
<span class="step-num" style="left:105px;top:2390px">1</span>
<div class="step-card" style="left:292px;top:2650px;width:523px;height:212px;padding:20px 0 0 52px">
  <h3>Get Setup</h3>
  <ul><li>• Input Your Alerts</li><li>• Input Your Staff</li><li>• Install Our Software</li></ul>
</div>
<span class="step-num" style="left:267px;top:2617px">2</span>
<div class="step-card" style="left:540px;top:2913px;width:523px;height:241px;padding:26px 0 0 43px">
  <h3>Feel Confident Your<br>Staff Is Protected</h3>
  <p style="font-size:20px;line-height:29px;font-weight:600;margin-top:14px;width:440px">High Five. You just too a major step to getting rid of the anxiety and frustration this gave you.</p>
</div>
<span class="step-num" style="left:514px;top:2877px">3</span>
<a class="btn btn-blue" href="#" style="left:437px;top:3216px;width:327px;height:70px">START MY DEMO</a>

<section class="cta-band">
  <p>Stay Connected with Staff during a Crisis Situations</p>
  <a class="btn btn-white" href="#" style="left:882px;top:31px;width:181px;height:46px;font-size:18px">Start My Demo</a>
</section>

<footer class="site-footer"></footer>
<div class="foot-col" style="left:142px;top:3458px;width:300px">
  <h4>Call Us</h4>
  <p style="font-size:25px;font-weight:600;margin-bottom:14px">1 - 800 - 555 - 0148</p>
  <p style="font-size:12px;line-height:17px;font-weight:500">When employees feel alone during a threatening situation, we give them a way to let the right resources know that they need help so you can feel confident that your staff is protected.</p>
  <div style="display:flex;align-items:center;justify-content:center;gap:8px;margin-top:16px;font-size:25px;font-weight:500;color:#3d9ae0"><i style="width:32px;height:32px;border-radius:50%;background:#3d9ae0;display:block"></i>CrewBeacon</div>
</div>
<span class="foot-rule" style="left:501px"></span>
<div class="foot-col" style="left:500px;top:3458px;width:200px">
  <h4>Shop</h4>
  <ul><li>Add Ons</li><li>Start My Demo</li><li>Custom Quote</li><li>Start Trial</li></ul>
</div>
<span class="foot-rule" style="left:810px"></span>
<div class="foot-col" style="left:808px;top:3458px;width:200px">
  <h4>About</h4>
  <ul><li>Affiliates</li><li>Contact</li><li>Support</li><li>Existing Customers</li><li>Industries</li><li>Blog</li><li>FAQ</li></ul>
</div>
<div class="legal">
  <span class="abs" style="left:141px;top:16px">Privacy Policy | Terms of Use | End User License Agreement</span>
  <span class="abs" style="left:930px;top:16px">©CrewBeacon 2020</span>
</div>

</body>
</html>
```